Criminal Defense Lawyer needs business cards and stationary
Dunmore Law Office
Criminal Defense Lawyer needs business cards and stationary - Law
Creative Brief
Simple
Ray Dunmore
418 N Willowbend Ave Lincoln, IL 62871
ray@dunmorelawoffice.example
dunmorelawoffice.example
I would like a simple/modern design for the front side of my card. I am thinking simply my logo in white with a blue background (same blue as in my logo). Other background colors to be considered are black and gray. That said, please be creative, I am open to any cutting edge design as long as it is not busy.
On the reverse side I would like my contact information displayed to include: My Name (Ray Dunmore) Dunmore Law Office (optional depending on design of front of card) Phone: 217-555-0143 email: ray@dunmorelawoffice.example Website: DunmoreLawOffice.example I do not want my address included. I am looking to create a visually modern yet simple design that is not too busy for the eye.
tavrelk tavrelk
Update: I have decided to add an additional winner. I will pick two designs that include business card and stationary. Thanks for the submissions. Also, designers, I am launching a website design contest soon. Keep an eye out for that.
Mistake in Brief. Please use phone number 217-555-0176 when submitting designs. Thank you.

```html
<!DOCTYPE html>
<html lang="en">
<head>
<meta charset="utf-8">
<title>Dunmore Law Office – Business Cards</title>
<link rel="stylesheet" href="https://fonts.googleapis.com/css2?family=Michroma&display=swap">
<style>
  :root {
    --backdrop: #d9dcdd;
    --card: #0b0b0b;
    --ink: #ffffff;
    --ink-soft: #d6d6d6;
  }
  * { margin: 0; padding: 0; box-sizing: border-box; }
  html, body {
    width: 1200px;
    height: 799px;
    overflow: hidden;
  }
  body {
    background: var(--backdrop);
    font-family: "Michroma", sans-serif;
    color: var(--ink);
    position: relative;
  }
  .card {
    position: absolute;
    top: 256px;
    width: 500px;
    height: 286px;
    background: var(--card);
    border-radius: 4px;
    box-shadow: 0 6px 18px rgba(0,0,0,0.18);
    overflow: hidden;
  }
  .card--front { left: 70px; }
  .card--back  { left: 630px; }

  .wordmark {
    position: absolute;
    display: flex;
    align-items: center;
    gap: 14px;
  }
  .wordmark__dot {
    border-radius: 50%;
    background: var(--ink);
    flex: none;
  }
  .wordmark__text { line-height: 1; }
  .wordmark__name {
    display: block;
    letter-spacing: 0.06em;
    text-transform: uppercase;
  }
  .wordmark__sub {
    display: block;
    text-transform: uppercase;
    letter-spacing: 0.32em;
    margin-top: 8px;
    padding-top: 6px;
    border-top: 1px solid var(--ink);
  }

  .card--front .wordmark { left: 60px; top: 108px; }
  .card--front .wordmark__dot { width: 54px; height: 54px; }
  .card--front .wordmark__name { font-size: 26px; }
  .card--front .wordmark__sub { font-size: 7px; }

  .card--back .wordmark {
    left: 30px; top: 104px;
    width: 146px;
    flex-direction: column;
    align-items: center;
    gap: 12px;
    text-align: center;
  }
  .card--back .wordmark__dot { width: 40px; height: 40px; }
  .card--back .wordmark__name { font-size: 16px; }
  .card--back .wordmark__sub { font-size: 6px; }

  .divider {
    position: absolute;
    left: 200px;
    top: 50px;
    width: 1px;
    height: 186px;
    background: var(--ink);
  }
  .contact {
    position: absolute;
    left: 224px;
    top: 62px;
    right: 20px;
  }
  .contact__name {
    font-size: 15px;
    letter-spacing: 0.1em;
    text-transform: uppercase;
    margin-bottom: 34px;
    white-space: nowrap;
  }
  .contact__row {
    display: flex;
    align-items: center;
    gap: 9px;
    font-size: 7px;
    letter-spacing: 0.02em;
    color: var(--ink-soft);
    text-transform: uppercase;
    margin-bottom: 24px;
    white-space: nowrap;
  }
  .contact__icon { width: 17px; height: 17px; flex: none; }
</style>
</head>
<body>
  <section class="card card--front" aria-label="Business card front">
    <div class="wordmark">
      <span class="wordmark__dot"></span>
      <span class="wordmark__text">
        <span class="wordmark__name">Dunmore</span>
        <span class="wordmark__sub">Law Office</span>
      </span>
    </div>
  </section>

  <section class="card card--back" aria-label="Business card back">
    <div class="wordmark">
      <span class="wordmark__dot"></span>
      <span class="wordmark__text">
        <span class="wordmark__name">Dunmore</span>
        <span class="wordmark__sub">Law Office</span>
      </span>
    </div>
    <div class="divider"></div>
    <div class="contact">
      <p class="contact__name">Ray Dunmore</p>
      <p class="contact__row">
        <svg class="contact__icon" viewBox="0 0 18 18" aria-hidden="true">
          <circle cx="9" cy="9" r="8.5" fill="#ffffff"/>
          <path d="M6.2 4.6l1.6 0.3 0.6 2-1 0.9c0.5 1.2 1.5 2.2 2.7 2.7l0.9-1 2 0.6 0.3 1.6c-0.4 0.7-1.2 1.1-2 0.9-3-0.8-5.1-2.9-5.9-5.9-0.2-0.8 0.2-1.6 0.8-2.1z" fill="#0b0b0b"/>
        </svg>
        217-555-0176
      </p>
      <p class="contact__row">
        <svg class="contact__icon" viewBox="0 0 18 18" aria-hidden="true">
          <circle cx="9" cy="9" r="8.5" fill="#ffffff"/>
          <rect x="4.5" y="5.8" width="9" height="6.4" rx="0.6" fill="#0b0b0b"/>
          <path d="M4.9 6.3L9 9.4l4.1-3.1" fill="none" stroke="#ffffff" stroke-width="0.8"/>
        </svg>
        ray@dunmorelawoffice.example
      </p>
    </div>
  </section>
</body>
</html>
```